Austin TX First Veterinary Urgent Care

We need a flyer designed for us and our clinic that is eye-catching but also summarizes the advantages of our services. We want to express that we are family owned, have convenient hours and affordable prices. We are the first veterinary urgent care animal clinic in Austin Texas. Our hours of operation are M-F 12PM-9PM S-S 10AM-6PM. Our Address is 48150 W Corvel Rd Suite B262 Austin, Tx 78699. Our phone number is (737)555-0148 our website is www.brindlepawclinic.example and our email address is info@brindlepawclinic.example.

Target Market(s)

Pet owners and veterinary professionals for referral purposes.

Industry/Entity Type

Veterinary

Font styles to use
Sans Serif

Colors
0094D4
00A9DD
6FCCEA
C7EBF8
E9F6FB
00AB8E
00BBA5
67D7C9
C6EFE9
E9F9F6

Requirements
Must have
• Our logo, hours of operation and contact information easy to read. Should emphasize that we are affordable as well as family owned. List of services should also be displayed: ear, eye, and skin issues, limping, broken toenails, lacerations, coughing, sneezing, allergies, vomiting and diarrhea, urinary issues, constipation, snake bites, toxin ingestion, and many many more
Nice to have
• We would like to have a modern feel with drawn/cartoon images, not realistic stock photos of dogs/cats.

```html
<!DOCTYPE html>
<html lang="en">
<head>
<meta charset="utf-8">
<title>Brindle Paw – Veterinary Urgent Care Flyer</title>
<link href="https://fonts.googleapis.com/css2?family=Poppins:wght@600;700;800&family=Roboto:wght@500;700;900&display=swap" rel="stylesheet">
<style>
  :root {
    --navy: #27286e;
    --green: #44ac5a;
    --paper: #f4f3ef;
    --mist: #d6dbd9;
    --sage: #b5c1bd;
    --teal-grey: #8ea8a4;
    --salmon: #d8a393;
    --white: #ffffff;
  }
  * { margin: 0; padding: 0; box-sizing: border-box; }
  html, body { width: 927px; height: 1200px; overflow: hidden; background: var(--paper); }
  .flyer {
    position: relative; width: 927px; height: 1200px; overflow: hidden;
    background: var(--paper); font-family: "Roboto", Arial, sans-serif; color: var(--navy);
  }
  .backdrop { position: absolute; inset: 0; }
  .brand {
    position: absolute; left: 70px; top: 160px; display: flex; align-items: center; gap: 14px;
  }
  .brand-dot { width: 42px; height: 42px; border-radius: 50%; background: var(--green); }
  .brand-name {
    font-family: "Poppins", Arial, sans-serif; font-weight: 800; font-size: 46px;
    color: var(--navy); letter-spacing: -1px;
  }
  .contact { position: absolute; left: 568px; top: 56px; }
  .contact-row { display: flex; align-items: center; gap: 14px; height: 37px; }
  .contact-row svg { width: 24px; height: 24px; flex: none; }
  .contact-row span { font-family: "Poppins", Arial, sans-serif; font-weight: 700; font-size: 18px; white-space: nowrap; }
  .contact-row.phone { height: 50px; }
  .contact-row.phone span { font-size: 31px; font-weight: 800; }
  .hours {
    position: absolute; left: 567px; top: 212px; width: 302px; height: 178px;
    background: var(--navy); border-radius: 16px; color: var(--white); text-align: center;
    padding-top: 18px;
  }
  .hours-day { color: var(--green); font-size: 23px; font-weight: 500; }
  .hours-time { font-size: 23px; font-weight: 500; margin-bottom: 8px; }
  .hours-rule { width: 190px; height: 1px; background: rgba(255,255,255,0.25); margin: 0 auto 10px; }
  .values {
    position: absolute; left: 89px; top: 359px; color: var(--green);
    font-weight: 700; font-size: 21px;
  }
  .headline {
    position: absolute; left: 83px; top: 396px; font-family: "Poppins", Arial, sans-serif;
    font-weight: 800; font-size: 53px; line-height: 57px; color: var(--navy); letter-spacing: -0.5px;
  }
  .headline .accent { color: var(--green); font-size: 66px; }
  .illustration { position: absolute; left: 540px; top: 475px; width: 387px; height: 725px; }
  .services {
    position: absolute; left: 62px; top: 618px; width: 563px; height: 320px;
    background: var(--white); border-radius: 36px; padding: 38px 0 0 45px;
  }
  .services h2 {
    font-weight: 900; font-size: 29px; color: var(--green); margin-bottom: 10px;
  }
  .service-cols { display: flex; gap: 36px; }
  .service-list { list-style: none; }
  .service-list li {
    position: relative; padding-left: 17px; font-size: 15.5px; font-weight: 500;
    height: 30.3px; line-height: 30px; letter-spacing: 0.2px;
  }
  .service-list li::before {
    content: ""; position: absolute; left: 0; top: 12px; width: 4px; height: 4px;
    border-radius: 50%; background: var(--green);
  }
  .service-list li.more::before { display: none; }
  .tagline {
    position: absolute; left: 82px; top: 958px; font-size: 21.5px; font-weight: 500; line-height: 28px;
  }
  .address-band {
    position: absolute; left: 62px; top: 1072px; width: 480px; height: 140px;
    background: var(--navy); border-radius: 36px 0 0 0;
    display: flex; align-items: flex-start; padding: 30px 0 0 40px; gap: 20px; color: var(--white);
  }
  .address-band svg { width: 30px; height: 46px; flex: none; margin-top: 4px; }
  .address-band p { font-family: "Poppins", Arial, sans-serif; font-weight: 700; font-size: 22px; line-height: 30px; }
</style>
</head>
<body>
<div class="flyer">
  <svg class="backdrop" width="927" height="1200" viewBox="0 0 927 1200" aria-hidden="true">
    <circle cx="-10" cy="-10" r="108" fill="var(--salmon)"/>
    <path d="M0 380 C 200 480, 420 560, 620 590 C 760 610, 860 520, 927 430 L927 1200 L0 1200 Z" fill="var(--mist)"/>
    <path d="M0 940 C 180 920, 380 980, 560 950 C 700 925, 820 880, 927 860 L927 1200 L0 1200 Z" fill="var(--sage)"/>
    <path d="M0 1050 C 160 1010, 360 1060, 540 1030 L540 1200 L0 1200 Z" fill="var(--teal-grey)"/>
  </svg>

  <div class="brand">
    <div class="brand-dot"></div>
    <div class="brand-name">Brindle Paw</div>
  </div>

  <div class="contact">
    <div class="contact-row">
      <svg viewBox="0 0 24 24" fill="none" stroke="var(--green)" stroke-width="1.6"><circle cx="12" cy="12" r="10"/><ellipse cx="12" cy="12" rx="4.5" ry="10"/><path d="M2 12h20M4 7h16M4 17h16"/></svg>
      <span>www.brindlepawclinic.example</span>
    </div>
    <div class="contact-row">
      <svg viewBox="0 0 24 24" fill="none" stroke="var(--green)" stroke-width="1.6"><rect x="2" y="5" width="20" height="14"/><path d="M2 5l10 8 10-8M2 19l7-7M22 19l-7-7"/></svg>
      <span>info@brindlepawclinic.example</span>
    </div>
    <div class="contact-row phone">
      <svg viewBox="0 0 24 24" fill="var(--green)"><path d="M6.6 10.8a15.1 15.1 0 0 0 6.6 6.6l2.2-2.2a1 1 0 0 1 1-.25 11.4 11.4 0 0 0 3.6.57 1 1 0 0 1 1 1V20a1 1 0 0 1-1 1A17 17 0 0 1 3 4a1 1 0 0 1 1-1h3.5a1 1 0 0 1 1 1c0 1.25.2 2.45.57 3.57a1 1 0 0 1-.25 1z"/></svg>
      <span>(737)555-0148</span>
    </div>
  </div>

  <div class="hours">
    <div class="hours-day">Monday-Friday</div>
    <div class="hours-time">12:00pm-9:00pm</div>
    <div class="hours-rule"></div>
    <div class="hours-day">Saturday-Sunday</div>
    <div class="hours-time">10:00am-6:00pm</div>
  </div>

  <div class="values">FAMILY OWNED • AFFORDABLE</div>
  <h1 class="headline">Getting Austin's<br>pets back on their<br>paws, <span class="accent">FAST</span></h1>

  <svg class="illustration" viewBox="0 0 387 725" role="img" aria-label="Cartoon illustration of a veterinarian in green scrubs examining a fluffy pink poodle with a stethoscope">
    <defs>
      <linearGradient id="illusFill" x1="0" y1="0" x2="0" y2="1">
        <stop offset="0" stop-color="#3b3c86"/>
        <stop offset="0.35" stop-color="#4cae60"/>
        <stop offset="1" stop-color="#d6a595"/>
      </linearGradient>
    </defs>
    <path d="M170 0 H387 V725 H60 C 40 600, 80 520, 130 460 C 170 380, 170 200, 170 0 Z" fill="url(#illusFill)" opacity="0.9"/>
  </svg>

  <section class="services">
    <h2>OUR SERVICES</h2>
    <div class="service-cols">
      <ul class="service-list">
        <li>EAR,EYE, &amp; SKIN ISSUES</li>
        <li>LIMPING</li>
        <li>BROKEN TOENAILS</li>
        <li>LACERATIONS</li>
        <li>COUGHING</li>
        <li>SNEEZING</li>
        <li>ALLERGIES</li>
      </ul>
      <ul class="service-list">
        <li>VOMITING &amp; DIARRHEA</li>
        <li>URINARY ISSUES</li>
        <li>CONSTIPATION</li>
        <li>SNAKE BITES</li>
        <li>TOXIN INGESTION</li>
        <li class="more">&amp; MANY MANY MORE</li>
      </ul>
    </div>
  </section>

  <p class="tagline">Urgent Care veterinary services at a<br>fraction of the cost of an Emergency visit.</p>

  <div class="address-band">
    <svg viewBox="0 0 30 46"><path d="M15 1C7 1 1 7 1 15c0 10 14 29 14 29s14-19 14-29C29 7 23 1 15 1z" fill="var(--green)"/><circle cx="15" cy="15" r="5.5" fill="var(--navy)"/></svg>
    <p>48150 W Corvel Rd Suite B262<br>Austin,Tx 78699</p>
  </div>
</div>
</body>
</html>
```